Website design for dressage horse training business

Looking to develop a new website design for a dressage horse training website. We want to change from a single landing page to one with multiple pages.
You are free to use your creativity to design the main landing page. This is the only page you need to design at this point. I would encourage looking at other Dressage Training websites to get a feel for what is typically on them. A few websites are listed below although I think the design of them could be better.
Notes:
- Menu to include: Home, Services, News Room, Blog, About Us, Contact,
- FAQ section on main page
- Logo to remain the same - the logo attached is not the correct color so change to match existing color.
- Change 'Sponsors' to 'Partnerships' on main page
Here is the link to the current site:
https://larkvalebarn.com/
Example sites
https://www.quillbrookstablesna.com/
https://corinnahaldwickdressage.com/
Older women with disposable income

```html
<!DOCTYPE html>
<html lang="en">
<head>
<meta charset="utf-8">
<title>Larkvale Barn — Dressage and Sport Horse Training</title>
<link rel="stylesheet" href="https://fonts.googleapis.com/css2?family=Mulish:ital,wght@0,400;0,600;0,700;1,600;1,800&display=swap">
<style>
:root{
  --tan:#c49a6c;
  --tan-light:#e8d9c7;
  --ink:#161616;
  --text:#333;
  --cream:#f5efe8;
  --maroon:#5c0c0c;
  --black:#050505;
  --white:#fff;
  --badge:#e4e0db;
}
*{box-sizing:border-box;margin:0;padding:0}
html,body{width:1200px;height:3884px;overflow:hidden;background:var(--white);font-family:"Mulish",sans-serif;color:var(--text)}
.page{position:relative;width:1200px;height:3884px;overflow:hidden}
.abs{position:absolute}
.heading{font-family:"Mulish",sans-serif;font-style:italic;font-weight:800;color:var(--ink)}
.body-copy{font-size:12.5px;line-height:23px;color:#3a3a3a}
.body-copy p+p{margin-top:6px}
.shadow{box-shadow:0 2px 14px rgba(0,0,0,.12);background:var(--white)}
.btn{display:flex;align-items:center;justify-content:center;font-size:15px;color:var(--white)}

/* header */
.brand{left:134px;top:6px;width:190px;color:var(--tan);font-weight:400;text-align:center}
.brand .word{font-size:40px;letter-spacing:-1px;line-height:44px}
.brand .sub{font-size:13px;letter-spacing:16px;line-height:16px;margin-left:12px}
.nav{left:523px;top:44px;font-size:14px;color:var(--ink)}
.nav span{position:absolute;white-space:nowrap}
.nav .active{color:var(--tan)}
.nav-dot{left:531px;top:17px;width:14px;height:18px;border-radius:50%;background:var(--tan-light)}
.contact-btn{left:894px;top:27px;width:155px;height:38px;background:var(--tan);font-size:15px}

/* hero */
.hero{left:0;top:77px;width:1200px;height:494px;background:linear-gradient(180deg,#4c5a3a 0%,#6b6a55 40%,#3e3a2e 75%,#111 100%)}
.hero-title{left:0;top:425px;width:1190px;text-align:center;color:var(--white);font-size:40px;line-height:47px}

/* training */
.photo{background:linear-gradient(160deg,#7a8a5c,#5a4a38 60%,#2d241c)}
.training-photo{left:134px;top:644px;width:537px;height:393px}
.training-card{left:516px;top:755px;width:535px;height:367px;padding:30px 30px 0}
.training-card h2{font-size:33px;margin-bottom:10px}
.know-btn{position:absolute;left:30px;top:311px;width:156px;height:36px;background:var(--tan)}

/* lessons */
.lessons-ghost{left:330px;top:1180px;font-size:112px;font-weight:800;color:#f3f3f3;letter-spacing:2px}
.lessons-title{left:211px;top:1222px;font-size:32px}
.lessons-rule{left:466px;top:1221px;width:2px;height:46px;background:var(--tan)}
.lessons-text{left:496px;top:1196px;width:490px;font-size:12.5px;line-height:23px;color:var(--ink);font-weight:600}
.lessons-text em{display:block;margin-top:8px;font-weight:600}

/* partnerships */
.partner-photo{left:134px;top:1369px;width:255px;height:377px;border-radius:4px;background:linear-gradient(180deg,#5b5e52,#b8aa8e 45%,#cbbfa6)}
.partner-title{left:436px;top:1362px;font-size:33px}
.partner-rule{left:445px;top:1447px;width:2px;height:151px;background:var(--tan)}
.badge{left:470px;width:142px;height:54px;border-radius:6px;background:var(--badge)}
.faint-brand{left:678px;top:1456px;width:352px;text-align:center;color:#eadccb}
.faint-brand .word{font-size:96px;line-height:100px;letter-spacing:-3px}
.faint-brand .sub{font-size:24px;letter-spacing:44px;margin-left:40px}
.partner-card{left:440px;top:1643px;width:612px;height:199px;padding:19px 17px 0}
.partner-card .name{color:var(--maroon);font-weight:700}
.visit-btn{position:absolute;left:17px;top:146px;width:129px;height:37px;background:var(--maroon)}

/* mission */
.mission{left:167px;top:1922px;width:851px;height:109px;background:var(--cream);display:flex;align-items:center;justify-content:center;text-align:center;padding:0 18px;font-size:13.5px;line-height:25px;color:var(--ink)}

/* for sale */
.sale-photo{left:514px;top:2100px;width:537px;height:396px;background:linear-gradient(150deg,#9aa87a,#5d4a35 50%,#2a1c14)}
.sale-vertical{left:1002px;top:2116px;writing-mode:vertical-rl;font-size:38px;color:#8b8b8b;letter-spacing:2px}
.sale-card{left:134px;top:2213px;width:537px;height:366px;padding:36px 27px 0}
.sale-card h2{font-size:33px;margin-bottom:14px}

/* faq */
.faq-title{left:0;top:2648px;width:1186px;text-align:center;font-size:33px}
.faq-photo{left:134px;top:2720px;width:455px;height:378px;background:linear-gradient(180deg,#7a4a2a 0%,#a0673a 40%,#e6ddd0 70%,#efe8de)}
.faq-item{left:610px;width:433px;height:41px;padding:0 17px;display:flex;align-items:center;justify-content:space-between;font-size:12px;color:var(--tan)}
.faq-item svg{flex:none}
.faq-open{left:610px;top:2723px;width:433px;height:77px;padding:13px 17px}
.faq-open .q{font-size:12px;color:var(--tan)}
.faq-open .a{font-size:10.5px;line-height:19px;color:#333;margin-top:3px}

/* contact */
.contact-band{left:0;top:3184px;width:1200px;height:310px;background:var(--cream)}
.contact-title{left:0;top:3254px;width:1186px;text-align:center;font-size:33px}
.contact-sub{left:200px;top:3320px;width:786px;text-align:center;font-size:17px;line-height:31px;font-style:italic;font-weight:600;color:var(--ink)}
.tan-box{left:412px;top:3384px;width:155px;height:38px;background:var(--tan)}
.or{left:578px;top:3388px;font-size:24px;color:var(--ink)}
.phone-btn{left:617px;top:3384px;width:155px;height:38px;background:var(--black);gap:8px}

/* footer */
.footer{left:0;top:3494px;width:1200px;height:390px;background:var(--black)}
.foot-h{font-size:17px;color:var(--tan)}
.foot-about{left:134px;top:3611px;width:336px;font-size:12.5px;line-height:23px;color:#e6e6e6}
.foot-about .more{color:var(--tan)}
.foot-item{left:552px;display:flex;gap:12px;font-size:12.5px;line-height:20px;color:#e6e6e6}
.foot-icon{width:30px;height:30px;border:1.5px solid var(--tan);border-radius:50%;display:flex;align-items:center;justify-content:center;flex:none}
.foot-brand{left:826px;top:3592px;width:225px;text-align:center;color:var(--tan)}
.foot-brand .word{font-size:58px;line-height:62px;letter-spacing:-2px}
.foot-brand .sub{font-size:17px;letter-spacing:28px;margin-left:24px}
.social{top:3696px;width:30px;height:30px;border:1.5px solid #777}
.foot-rule{left:134px;top:3829px;width:917px;height:1px;background:#333}
.copyright{left:0;top:3847px;width:1186px;text-align:center;font-size:12.5px;color:#e6e6e6}
</style>
</head>
<body>
<div class="page">

  <!-- header -->
  <div class="abs brand"><div class="word">LARKVALE</div><div class="sub">BARN</div></div>
  <div class="abs nav-dot"></div>
  <div class="abs nav">
    <span class="active" style="left:0">Home</span>
    <span style="left:75px">Services</span>
    <span style="left:161px">News</span>
    <span style="left:231px;top:-2px">Blog</span>
    <span style="left:291px">About Us</span>
  </div>
  <div class="abs btn contact-btn">Contact Us Today</div>

  <!-- hero -->
  <div class="abs hero" role="img" aria-label="Rider in navy jacket on a paint horse beside a wooden barn"></div>
  <h1 class="abs heading hero-title" style="color:#fff">Central Iowa’s Premier<br>Dressage And Sport Horse Training</h1>

  <!-- training -->
  <div class="abs photo training-photo" role="img" aria-label="Rider on a bay horse in a grass paddock"></div>
  <section class="abs shadow training-card">
    <h2 class="heading">Horse Training</h2>
    <div class="body-copy">
      <p>Larkvale Barn offers both full and half time training options with Hattie Brennard. There is much flexibility with both rides and/or lessons weekly in the training packages that can be customized to fit both the horse and the rider’s needs.</p>
      <p>Generally, full training provides 3-4 “working days” of riding, and 1-2 “light” days consisting of cavelletti/jumping, hacking or lunging depending on the horse’s personality, their needs, and the training goals.</p>
      <p>Hattie’s empathetic and cross-training techniques create horses who are happy and content in their jobs, while building strength and endurance for the dressage ring.</p>
    </div>
    <div class="btn know-btn">Know More</div>
  </section>

  <!-- lessons -->
  <div class="abs lessons-ghost" aria-hidden="true">LESSONS</div>
  <h2 class="abs heading lessons-title">Horse Lessions</h2>
  <div class="abs lessons-rule"></div>
  <div class="abs lessons-text">Lessons are available for all ages of riders. Hattie thoroughly enjoys working with accomplished riders looking to succeed in the show ring, as well as riders just wanting to learn what dressage is about.<em>Come join our incredible and encouraging team!</em></div>

  <!-- partnerships -->
  <div class="abs partner-photo" role="img" aria-label="Trainer in a patterned show shirt standing in an arena"></div>
  <h2 class="abs heading partner-title">Our Partnerships With</h2>
  <div class="abs partner-rule"></div>
  <div class="abs badge" style="top:1440px" role="img" aria-label="Ardent Saddlery partner badge"></div>
  <div class="abs badge" style="top:1526px" role="img" aria-label="Merriweather Saddlery partner badge"></div>
  <div class="abs faint-brand" aria-hidden="true"><div class="word">LARKVALE</div><div class="sub">BARN</div></div>
  <section class="abs shadow partner-card">
    <div class="body-copy">
      <p><span class="name">Ardent Saddlery</span> is constantly designing and researching saddles and riders to find the right blend of design and craftsmanship to fit today’s demands. Every saddle’s detail is carefully checked to be sure the workmanship and quality is there.</p>
      <p>&nbsp;All saddles are anatomically designed for horse and rider, hand-crafted from the finest leathers, and manufactured using the most technically advanced methods and features available.</p>
    </div>
    <div class="btn visit-btn">Visit Webiste</div>
  </section>

  <!-- mission -->
  <div class="abs mission">Our misssion lorem ipsum dolor sit amet, consectetuer adipiscing elit, sed diam nonummy nibh euismod tincidunt ut laoreet dolore magna aliquam erat volt wisi enim ad minim veniam, quis nostrud exerci tation ullamcorper suscipit lobortis.</div>

  <!-- for sale -->
  <div class="abs sale-photo" role="img" aria-label="Dark bay horse head with braided mane"></div>
  <div class="abs sale-vertical">Winslow's Reverie</div>
  <section class="abs shadow sale-card">
    <h2 class="heading">Horse For Sale</h2>
    <div class="body-copy">
      <p>Winslow's Reverie, “Wren,” (Callisto x Regent Star) is a 2012, 16hh imported Hanoverian. Wren is an incredibly quiet and kind horse. He is ridden by both an amatuer and child rider. He loves to hack and is very quiet alone and with a group of horses.&nbsp; He has shown through first level with scores into the 70’s at both training and first level. Wren is currently solidly schooling all of second level, as well as half passes and flying changes from third level.</p>
      <p>Wren has 3 very easy to ride gaits and it is easy for riders to sit his trot. Very quiet and well mannered on the ground with vet, farrier and clipping. He has lovely confirmation with a striking head. He is regularly admired at shows! Wren is very versatile and game and also loves to jump!</p>
    </div>
  </section>

  <!-- faq -->
  <h2 class="abs heading faq-title">Frequently Asked Questions</h2>
  <div class="abs faq-photo" role="img" aria-label="Chestnut horse legs trotting on sand with a speech bubble reading FAQs"></div>
  <div class="abs shadow faq-open">
    <div class="q">Diam nonummy nibh euismod tincidunt ut laoreet&nbsp; ?</div>
    <div class="a">Lorem ipsum dolor sit amet, consectetuer adipiscing elit, sed diam nonummy nibh euismod tincidunt ut laoreet dolore magn.</div>
  </div>
  <div class="abs shadow faq-item" style="top:2807px">What paperwork do I need to donate my Horse<svg width="10" height="6" viewBox="0 0 10 6"><path d="M1 1l4 4 4-4" fill="none" stroke="#c49a6c" stroke-width="1.3"/></svg></div>
  <div class="abs shadow faq-item" style="top:2857px">Laoreet dolore magna aliquam erat fdsf ?<svg width="10" height="6" viewBox="0 0 10 6"><path d="M1 1l4 4 4-4" fill="none" stroke="#c49a6c" stroke-width="1.3"/></svg></div>
  <div class="abs shadow faq-item" style="top:2907px">Dolor sit amet consectetuer adipiscing elit ?<svg width="10" height="6" viewBox="0 0 10 6"><path d="M1 1l4 4 4-4" fill="none" stroke="#c49a6c" stroke-width="1.3"/></svg></div>
  <div class="abs shadow faq-item" style="top:2957px">Lorem ipsum dolor sit amet consectetuer adipiscing elit ?<svg width="10" height="6" viewBox="0 0 10 6"><path d="M1 1l4 4 4-4" fill="none" stroke="#c49a6c" stroke-width="1.3"/></svg></div>
  <div class="abs shadow faq-item" style="top:3007px">Dolor sit amet consectetuer adipiscing elit ?<svg width="10" height="6" viewBox="0 0 10 6"><path d="M1 1l4 4 4-4" fill="none" stroke="#c49a6c" stroke-width="1.3"/></svg></div>
  <div class="abs shadow faq-item" style="top:3057px">Lorem ipsum dolor sit amet consectetuer adipiscing elit ?<svg width="10" height="6" viewBox="0 0 10 6"><path d="M1 1l4 4 4-4" fill="none" stroke="#c49a6c" stroke-width="1.3"/></svg></div>

  <!-- contact -->
  <div class="abs contact-band"></div>
  <h2 class="abs heading contact-title">Contact Me</h2>
  <p class="abs contact-sub">If you are interested in learning more about Larkvale Barn’s services or availability for training or lessons, please contact us below!</p>
  <div class="abs tan-box"></div>
  <div class="abs or">Or</div>
  <div class="abs btn phone-btn">
    <svg width="18" height="18" viewBox="0 0 24 24"><path d="M6.6 10.8a15 15 0 0 0 6.6 6.6l2.2-2.2a1 1 0 0 1 1-.25 11.4 11.4 0 0 0 3.6.6 1 1 0 0 1 1 1V20a1 1 0 0 1-1 1A17 17 0 0 1 3 4a1 1 0 0 1 1-1h3.5a1 1 0 0 1 1 1c0 1.25.2 2.45.6 3.6a1 1 0 0 1-.25 1z" fill="none" stroke="#c49a6c" stroke-width="1.6"/></svg>
    <span style="color:#c49a6c">515-555-0187</span>
  </div>

  <!-- footer -->
  <footer class="abs footer"></footer>
  <div class="abs foot-h" style="left:137px;top:3574px">About Larkvale Barn</div>
  <p class="abs foot-about">FEI rider and trainer, Hattie Brennard began her riding career at a young age. She went up through the ranks of Pony Club and with an emphasis &amp; focus in eventing. During college, Hattie worked for a small breeder starting young horses. Hattie loves starting young horses including starting and guiding them in a correct and quiet way to help them flourish….<span class="more">Read More</span></p>
  <div class="abs foot-h" style="left:552px;top:3574px">Contact Details</div>
  <div class="abs foot-item" style="top:3618px">
    <div class="foot-icon"><svg width="12" height="15" viewBox="0 0 12 15"><path d="M6 14s5-5 5-8.5a5 5 0 0 0-10 0C1 9 6 14 6 14z" fill="none" stroke="#c49a6c" stroke-width="1.2"/><circle cx="6" cy="5.5" r="1.8" fill="none" stroke="#c49a6c" stroke-width="1.2"/></svg></div>
    <div style="margin-left:4px">Larkvale Barn<br>Ashford, IA 50399</div>
  </div>
  <div class="abs foot-item" style="top:3676px">
    <div class="foot-icon"><svg width="14" height="14" viewBox="0 0 24 24"><path d="M6.6 10.8a15 15 0 0 0 6.6 6.6l2.2-2.2a1 1 0 0 1 1-.25 11.4 11.4 0 0 0 3.6.6 1 1 0 0 1 1 1V20a1 1 0 0 1-1 1A17 17 0 0 1 3 4a1 1 0 0 1 1-1h3.5a1 1 0 0 1 1 1c0 1.25.2 2.45.6 3.6a1 1 0 0 1-.25 1z" fill="none" stroke="#c49a6c" stroke-width="2"/></svg></div>
    <div>Phone<br>515.555.0187</div>
  </div>
  <div class="abs foot-item" style="top:3734px">
    <div class="foot-icon"><svg width="14" height="11" viewBox="0 0 14 11"><rect x="1" y="1" width="12" height="9" fill="none" stroke="#c49a6c" stroke-width="1.2"/><path d="M1 1l6 5 6-5" fill="none" stroke="#c49a6c" stroke-width="1.2"/></svg></div>
    <div style="margin-left:4px">Email<br>inquiry@larkvalebarn.com</div>
  </div>
  <div class="abs foot-brand"><div class="word">LARKVALE</div><div class="sub">BARN</div></div>
  <div class="abs social" style="left:870px"></div>
  <div class="abs social" style="left:905px"></div>
  <div class="abs social" style="left:941px"></div>
  <div class="abs social" style="left:976px"></div>
  <div class="abs foot-rule"></div>
  <div class="abs copyright">Copyright © 2021 Larkvale Barn. All Rights Reserved.</div>

</div>
</body>
</html>
```